Brivora Collective Business Card Design

We need a business card design for Brivora Collective. We are a healthcare recruiting, wellness and education company. We partner with medical facilities to find quality candidates. We also offer free wellness courses.
The final design should communicate an emphasis on recruiting and wellness
The main purpose of the business card is to utilized it for networking events, give to hospitals, executives, VCs surgery centers and clinics. I want it to be sleek, clean, use of our brand colors and professional.

```html
<!DOCTYPE html>
<html lang="en">
<head>
<meta charset="utf-8">
<title>Brivora Collective Business Card</title>
<link href="https://fonts.googleapis.com/css2?family=Lato:wght@400;700;900&display=swap" rel="stylesheet">
<style>
  :root {
    --teal-deep: #02554f;
    --teal-mid: #0b7a70;
    --teal-bright: #1fd8c6;
    --ink-grey: #6b6b6b;
    --card-white: #ffffff;
    --backdrop: #2b2b2b;
  }
  * { margin: 0; padding: 0; box-sizing: border-box; }
  html, body { width: 1200px; height: 875px; overflow: hidden; }
  body {
    background: var(--backdrop);
    font-family: "Lato", sans-serif;
    position: relative;
  }
  .card {
    position: absolute;
    top: 283px;
    width: 540px;
    height: 309px;
    border-radius: 16px;
    overflow: hidden;
  }
  /* Back side */
  .card-back {
    left: 40px;
    background: var(--teal-deep);
  }
  .back-pattern {
    position: absolute; inset: 0;
    background: linear-gradient(110deg, var(--teal-bright) 0%, var(--teal-mid) 28%, var(--teal-deep) 55%, #0a2d2a 100%);
  }
  .back-name {
    position: absolute;
    left: 0; right: 0; top: 140px;
    text-align: center;
    color: var(--card-white);
    font-weight: 900;
    font-size: 24px;
    letter-spacing: 0.5px;
  }
  /* Front side */
  .card-front {
    left: 620px;
    background: var(--card-white);
    color: var(--teal-deep);
  }
  .brand {
    position: absolute;
    right: 34px; top: 36px;
    display: flex; align-items: center; gap: 10px;
  }
  .brand-square {
    width: 22px; height: 22px;
    background: var(--teal-deep);
    border-radius: 4px;
  }
  .brand-name {
    font-size: 26px;
    font-weight: 400;
    color: var(--teal-deep);
  }
  .divider {
    position: absolute;
    height: 1px;
    background: var(--teal-deep);
  }
  .divider-top { left: 150px; right: 26px; top: 96px; }
  .divider-mid { left: 30px; width: 200px; top: 176px; }
  .person { position: absolute; left: 30px; top: 118px; }
  .person-name { font-size: 24px; font-weight: 900; letter-spacing: 0.3px; }
  .person-title { font-size: 14px; color: var(--ink-grey); margin-top: 2px; }
  .contacts {
    position: absolute; left: 30px; top: 186px;
    list-style: none;
    font-size: 12.5px; color: var(--ink-grey);
    line-height: 19px;
  }
  .contacts li { display: flex; align-items: center; gap: 9px; }
  .contacts svg { width: 11px; height: 11px; fill: var(--teal-deep); flex: none; }
  .address {
    position: absolute; right: 30px; top: 112px;
    text-align: right;
    font-size: 12.5px; color: var(--ink-grey);
    line-height: 19px;
  }
  .address-company { color: var(--teal-deep); font-weight: 700; }
  .band {
    position: absolute; left: 0; right: 0; bottom: 0;
    height: 14px;
  }
</style>
</head>
<body>
  <section class="card card-back">
    <div class="back-pattern" role="img" aria-label="Decorative pattern of scattered rounded tiles shading from bright aqua to deep teal"></div>
    <div class="back-name">Brivora Collective</div>
  </section>

  <section class="card card-front">
    <div class="brand">
      <span class="brand-square"></span>
      <span class="brand-name">Brivora Collective</span>
    </div>
    <div class="divider divider-top"></div>

    <div class="person">
      <div class="person-name">DANIEL REYES</div>
      <div class="person-title">Founder &amp; CEO</div>
    </div>
    <div class="divider divider-mid"></div>

    <ul class="contacts">
      <li><svg viewBox="0 0 24 24"><path d="M6.6 10.8a15.1 15.1 0 0 0 6.6 6.6l2.2-2.2a1 1 0 0 1 1-.25 11.4 11.4 0 0 0 3.6.57 1 1 0 0 1 1 1V20a1 1 0 0 1-1 1A17 17 0 0 1 3 4a1 1 0 0 1 1-1h3.5a1 1 0 0 1 1 1c0 1.25.2 2.45.57 3.6a1 1 0 0 1-.25 1z"/></svg>(555) 214-3380</li>
      <li><svg viewBox="0 0 24 24"><path d="M7 1h10a2 2 0 0 1 2 2v18a2 2 0 0 1-2 2H7a2 2 0 0 1-2-2V3a2 2 0 0 1 2-2zm0 3v14h10V4zm5 15.5a1 1 0 1 0 0 2 1 1 0 0 0 0-2z"/></svg>(555) 214-3381</li>
      <li><svg viewBox="0 0 24 24"><path d="M6 2h12v5H6zM4 8h16a2 2 0 0 1 2 2v7h-4v5H6v-5H2v-7a2 2 0 0 1 2-2zm4 8v4h8v-4z"/></svg>(555) 214-3382</li>
      <li><svg viewBox="0 0 24 24"><path d="M2 5h20v14H2zm2 2v.5l8 5 8-5V7z"/></svg>info@brivoracollective.com</li>
    </ul>

    <div class="address">
      <div class="address-company">Brivora Collective</div>
      <div>4870 Alder Court, Ste</div>
      <div>Fairhaven, CT 06520</div>
      <div>www.brivoracollective.com</div>
    </div>

    <svg class="band" viewBox="0 0 540 14" preserveAspectRatio="none">
      <polygon points="0,6 440,6 436,14 0,14" fill="var(--teal-deep)"/>
      <polygon points="446,0 540,0 540,14 440,14" fill="var(--teal-deep)"/>
    </svg>
  </section>
</body>
</html>
```